Need a Car Magnet designed

I need a car magnet designed.

The dimensions have to be 9" width by 2.6" height.

It needs to say PLOVA TRIP and include the attached logo

```html
<!DOCTYPE html>
<html lang="en">
<head>
<meta charset="utf-8">
<title>PLOVA TRIP – Car Magnet Options</title>
<link href="https://fonts.googleapis.com/css2?family=Cinzel:wght@700&family=Montserrat:wght@800&display=swap" rel="stylesheet">
<style>
  :root {
    --board-grey: #b1b1b1;
    --magnet-white: #ffffff;
    --pattern-tint: #f4f4f4;
    --tour-blue: #133b87;
    --badge-red: #d9330c;
    --badge-rim: #5a5a5a;
    --text-white: #ffffff;
  }
  * { margin: 0; padding: 0; box-sizing: border-box; }
  html, body {
    width: 1200px;
    height: 846px;
    overflow: hidden;
    background: var(--board-grey);
  }
  .presentation-board {
    position: relative;
    width: 1200px;
    height: 846px;
  }
  .car-magnet {
    position: absolute;
    left: 116px;
    width: 1007px;
    height: 290px;
    background: var(--magnet-white);
    overflow: hidden;
  }
  .car-magnet--serif { top: 88px; }
  .car-magnet--sans { top: 425px; }

  .golf-pattern {
    position: absolute;
    inset: 0;
    background: linear-gradient(180deg, var(--magnet-white), var(--pattern-tint));
  }
  .blue-band {
    position: absolute;
    left: 0;
    right: 0;
    top: 76px;
    height: 139px;
    background: var(--tour-blue);
  }
  .brand-seal {
    position: absolute;
    width: 236px;
    height: 236px;
    border-radius: 50%;
    background: var(--badge-red);
    border: 6px solid var(--badge-rim);
    box-shadow: 0 0 0 5px var(--magnet-white);
    display: flex;
    align-items: center;
    justify-content: center;
  }
  .car-magnet--serif .brand-seal { left: 72px; top: 26px; }
  .car-magnet--sans .brand-seal { left: 112px; top: 11px; }
  .brand-seal__name {
    color: var(--text-white);
    font-size: 30px;
    line-height: 1;
    letter-spacing: 1px;
  }
  .car-magnet--serif .brand-seal__name { font-family: "Cinzel", serif; font-weight: 700; }
  .car-magnet--sans .brand-seal__name { font-family: "Montserrat", sans-serif; font-weight: 800; }

  .magnet-title {
    position: absolute;
    top: 76px;
    height: 139px;
    display: flex;
    align-items: center;
    color: var(--text-white);
    white-space: nowrap;
    line-height: 1;
  }
  .car-magnet--serif .magnet-title {
    left: 359px;
    font-family: "Cinzel", serif;
    font-weight: 700;
    font-size: 80px;
    letter-spacing: 1px;
  }
  .car-magnet--sans .magnet-title {
    left: 400px;
    font-family: "Montserrat", sans-serif;
    font-weight: 800;
    font-size: 84px;
    letter-spacing: 1px;
  }
</style>
</head>
<body>
  <main class="presentation-board">
    <section class="car-magnet car-magnet--serif" aria-label="Car magnet option one">
      <div class="golf-pattern" role="img" aria-label="Faint line pattern of golf clubs, tees, bags and balls"></div>
      <div class="blue-band"></div>
      <div class="brand-seal"><span class="brand-seal__name">PLOVA TRIP</span></div>
      <h1 class="magnet-title">PLOVA TRIP</h1>
    </section>

    <section class="car-magnet car-magnet--sans" aria-label="Car magnet option two">
      <div class="golf-pattern" role="img" aria-label="Faint line pattern of golf clubs, tees, bags and balls"></div>
      <div class="blue-band"></div>
      <div class="brand-seal"><span class="brand-seal__name">PLOVA TRIP</span></div>
      <h2 class="magnet-title">PLOVA TRIP</h2>
    </section>
  </main>
</body>
</html>
```